Design for "Vellow" protein health bars wrappers

I need a new design for a protein bar that my partners and I are launching for the North American and European markets.
The bar's name is "Vellow."
Given the masculine/aggressive nature of that name, we are thinking of neutralizing it with a more feminine/soft font and design. But hey - the sky is the limit. We obviously want this 20-gram protein bar to sell to a wide net (not just men but women also). So if it means having a Pellam Comic font/design (or whatever) in order to do this, so be it. I leave it up to your intelligence and experience.

ADDED ON FEBRUARY 24:

The official name of the bar is just "VELLOW" (not "Vellow Protein").

We have six flavors divided into two categories, which are 1) SOFT and 2) CRUNCHY.
So, the idea is to make two similar designs for the wrapper that still distinguish themselves from each other because one is 'soft' and the other is 'crunchy.'
Then, within each category, the idea is to have three color variations, designating the three flavors in each category.

Please look at the dimensions and examples of the generic wrapper designs that we already have (and which we find too generic), which I have uploaded.

Target Market(s)

North America - Brindle, Fair Harvest
Europe - Norway, Sweden, Denmark, Germany, France, Switzerland, Italy.

Industry/Entity Type

Nutrition

Logo Text

Vellow

Font styles to use
Serif
Decorative

Colors
fff6dc
f04a50

Requirements
Must have
• The title is "Vellow".
• We have six flavors divided into two categories, which are 1) SOFT and 2) CRUNCHY.
• You can work on the two different types of similar-but-different designs for the "soft" and for the "cruncy." Then it's just a question of color variations for each flavor.
• The flavors are:
• SOFT: 1) strawberry, 2) Chocolate brownie, 3) Cinnamon Crunch
• CRUNCY: 1) Peanut, 2) Lemon, 3) Coconut.
• On the side or at the bottom, there should be stated:
• "20 gm protein"
• "children friendly"
Nice to have
• Obvious: a design that catches the eye and inspires someone to buy the bar to eat it.
• Part of the design could include a photograph of the actual bar (you can use generic photos for that until we place a pic of the actual bar). Like 1/4th of the total surface (or even a little smaller).

```html
<!DOCTYPE html>
<html lang="en">
<head>
<meta charset="utf-8">
<title>Vellow Nutrition Bar Wrappers</title>
<link rel="stylesheet" href="https://fonts.googleapis.com/css2?family=Abril+Fatface&family=Lora:ital,wght@0,400;0,700;1,400&family=Playfair+Display:wght@400;700&family=Caveat:wght@600&display=swap">
<style>
  :root {
    --canvas: #ffffff;
    --cream: #fff6dc;
    --crimp-cream: #f3e9cc;
    --coral: #f04a50;
    --ink-dark: #3a2a22;

    --plum: #4a1736;
    --plum-band: #9c2a8c;
    --plum-band-dark: #5b1b46;
    --plum-label: #8d2883;

    --coral-band: #f1c33d;
    --coral-band-dark: #d8353b;
    --coral-label: #f2c840;
    --coral-label-ink: #7a4a00;

    --badge-brown: #6b4a33;
    --badge-green: #2f9a46;
    --badge-olive: #3d3a2c;

    --brownie-dark: #3a1d12;
    --brownie-mid: #6a3a22;
    --brownie-light: #8c5533;
  }

  * { box-sizing: border-box; margin: 0; padding: 0; }

  html, body {
    width: 1200px;
    height: 965px;
    overflow: hidden;
    background: var(--canvas);
  }

  .stage { position: relative; width: 1200px; height: 965px; }
  .defs { position: absolute; width: 0; height: 0; }

  .wrapper {
    position: absolute;
    left: 110px;
    width: 980px;
    height: 320px;
    display: flex;
  }
  .wrapper--soft { top: 80px; }
  .wrapper--crunchy { top: 560px; }

  .crimp { width: 36px; height: 320px; flex: none; }
  .crimp--end { transform: scaleX(-1); color: var(--crimp-cream); }
  .wrapper--soft .crimp--start { color: var(--plum); }
  .wrapper--crunchy .crimp--start { color: var(--coral); }

  .wrapper__body { position: relative; flex: 1; height: 320px; display: flex; }

  .front { position: relative; width: 440px; height: 100%; }
  .wrapper--soft .front { background: var(--plum); }
  .wrapper--crunchy .front { background: var(--coral); }

  .category {
    position: absolute;
    left: 0;
    top: 34px;
    width: 100%;
    text-align: center;
    font-family: "Playfair Display", Georgia, serif;
    font-weight: 700;
    font-size: 16px;
    letter-spacing: 6px;
    color: var(--cream);
  }

  .brand {
    position: absolute;
    left: 0;
    top: 70px;
    width: 100%;
    text-align: center;
    font-family: "Abril Fatface", Georgia, serif;
    font-weight: 400;
    font-size: 92px;
    line-height: 1;
    color: var(--cream);
  }

  .product-label {
    position: absolute;
    left: 90px;
    top: 178px;
    width: 260px;
    height: 38px;
    font-family: "Caveat", cursive;
    font-weight: 600;
    font-size: 26px;
    line-height: 38px;
    text-align: center;
  }
  .wrapper--soft .product-label {
    background: var(--plum-label);
    color: var(--cream);
    border-radius: 19px;
  }
  .wrapper--crunchy .product-label {
    background: var(--coral-label);
    color: var(--coral-label-ink);
    clip-path: polygon(0 0, 100% 0, 94% 50%, 100% 100%, 0 100%, 6% 50%);
  }

  .claim {
    position: absolute;
    left: 0;
    top: 236px;
    width: 100%;
    text-align: center;
    font-family: "Lora", Georgia, serif;
    font-weight: 700;
    font-size: 17px;
    color: var(--cream);
  }

  .kids {
    position: absolute;
    left: 0;
    top: 266px;
    width: 100%;
    text-align: center;
    font-family: "Lora", Georgia, serif;
    font-style: italic;
    font-weight: 400;
    font-size: 17px;
    color: var(--cream);
  }

  .flavor-band {
    position: relative;
    height: 100%;
    display: flex;
    align-items: center;
    justify-content: center;
  }
  .flavor-band span {
    display: block;
    transform: rotate(-90deg);
    white-space: nowrap;
    color: var(--cream);
  }
  .flavor-band--main { width: 74px; font-family: "Playfair Display", Georgia, serif; font-weight: 400; font-size: 44px; }
  .flavor-band--sub { width: 54px; font-family: "Playfair Display", Georgia, serif; font-weight: 700; font-size: 32px; letter-spacing: 2px; }
  .wrapper--soft .flavor-band--main { background: var(--plum-band); }
  .wrapper--soft .flavor-band--sub { background: var(--plum-band-dark); }
  .wrapper--crunchy .flavor-band--main { background: var(--coral-band); }
  .wrapper--crunchy .flavor-band--main span { color: var(--ink-dark); }
  .wrapper--crunchy .flavor-band--sub { background: var(--coral-band-dark); }

  .panel { position: relative; flex: 1; height: 100%; background: var(--cream); }

  .badges { position: absolute; left: 40px; top: 22px; display: flex; gap: 14px; }
  .badge {
    width: 52px;
    height: 52px;
    border-radius: 50%;
    border: 3px solid var(--cream);
    box-shadow: 0 0 0 1px #d8ccb0;
  }
  .badge--natural { background: var(--badge-brown); }
  .badge--gluten { background: var(--badge-green); }
  .badge--vegan { background: var(--badge-olive); }

  .bar-photo {
    position: absolute;
    left: 14px;
    top: 92px;
    width: 200px;
    height: 210px;
    background: linear-gradient(160deg, var(--brownie-light) 0%, var(--brownie-mid) 45%, var(--brownie-dark) 100%);
  }
  .wrapper--soft .bar-photo { border-radius: 18px; }
  .wrapper--crunchy .bar-photo { border-radius: 0; }

  .protein-seal {
    position: absolute;
    left: 224px;
    top: 200px;
    width: 66px;
    height: 66px;
    border-radius: 50%;
    background: var(--coral);
    border: 3px solid var(--cream);
    box-shadow: 0 0 0 1px #d8ccb0;
    color: var(--cream);
    font-family: "Lora", Georgia, serif;
    text-align: center;
    display: flex;
    flex-direction: column;
    justify-content: center;
  }
  .protein-seal__value { font-weight: 700; font-size: 22px; line-height: 1; }
  .protein-seal__value small { font-size: 10px; }
  .protein-seal__label { font-weight: 700; font-size: 8px; letter-spacing: .5px; }

  .net-weight {
    position: absolute;
    left: 306px;
    top: 130px;
    transform: translate(-50%, -50%) rotate(90deg);
    white-space: nowrap;
    font-family: "Lora", Georgia, serif;
    font-size: 15px;
    color: var(--ink-dark);
  }
</style>
</head>
<body>
<main class="stage">
  <svg class="defs" aria-hidden="true">
    <symbol id="crimp-edge" viewBox="0 0 36 320" preserveAspectRatio="none">
      <polygon fill="currentColor" points="36,0 0,0 12,8 0,16 12,24 0,32 12,40 0,48 12,56 0,64 12,72 0,80 12,88 0,96 12,104 0,112 12,120 0,128 12,136 0,144 12,152 0,160 12,168 0,176 12,184 0,192 12,200 0,208 12,216 0,224 12,232 0,240 12,248 0,256 12,264 0,272 12,280 0,288 12,296 0,304 12,312 0,320 36,320"/>
      <line x1="22" y1="0" x2="22" y2="320" stroke="#000" stroke-opacity=".08" stroke-width="1"/>
      <line x1="29" y1="0" x2="29" y2="320" stroke="#000" stroke-opacity=".08" stroke-width="1"/>
    </symbol>
  </svg>

  <article class="wrapper wrapper--soft" aria-label="Vellow soft chocolate brownie wrapper">
    <svg class="crimp crimp--start"><use href="#crimp-edge"/></svg>
    <div class="wrapper__body">
      <section class="front">
        <p class="category">SOFT</p>
        <h1 class="brand">VELLOW</h1>
        <p class="product-label">Nutrition Bar</p>
        <p class="claim">no artificial preservatives or sweeteners</p>
        <p class="kids">children friendly</p>
      </section>
      <div class="flavor-band flavor-band--main"><span>Chocolate</span></div>
      <div class="flavor-band flavor-band--sub"><span>BROWNIE</span></div>
      <section class="panel">
        <div class="badges">
          <span class="badge badge--natural"></span>
          <span class="badge badge--gluten"></span>
          <span class="badge badge--vegan"></span>
        </div>
        <div class="bar-photo" role="img" aria-label="Photo of stacked chocolate brownie pieces"></div>
        <div class="protein-seal">
          <span class="protein-seal__value">20<small>gm</small></span>
          <span class="protein-seal__label">PROTEIN</span>
        </div>
        <p class="net-weight">Net. Wt. 2oz (54g)</p>
      </section>
    </div>
    <svg class="crimp crimp--end"><use href="#crimp-edge"/></svg>
  </article>

  <article class="wrapper wrapper--crunchy" aria-label="Vellow crunchy chocolate brownie wrapper">
    <svg class="crimp crimp--start"><use href="#crimp-edge"/></svg>
    <div class="wrapper__body">
      <section class="front">
        <p class="category">CRUNCHY</p>
        <h2 class="brand">VELLOW</h2>
        <p class="product-label">Nutrition Bar</p>
        <p class="claim">no artificial preservatives or sweeteners</p>
        <p class="kids">children friendly</p>
      </section>
      <div class="flavor-band flavor-band--main"><span>Chocolate</span></div>
      <div class="flavor-band flavor-band--sub"><span>BROWNIE</span></div>
      <section class="panel">
        <div class="badges">
          <span class="badge badge--natural"></span>
          <span class="badge badge--gluten"></span>
          <span class="badge badge--vegan"></span>
        </div>
        <div class="bar-photo" role="img" aria-label="Photo of stacked chocolate brownie pieces"></div>
        <div class="protein-seal">
          <span class="protein-seal__value">20<small>gm</small></span>
          <span class="protein-seal__label">PROTEIN</span>
        </div>
        <p class="net-weight">Net. Wt. 2oz (54g)</p>
      </section>
    </div>
    <svg class="crimp crimp--end"><use href="#crimp-edge"/></svg>
  </article>
</main>
</body>
</html>
```